Pricing Page; Request Quote Page Design

I'm looking to update our pricing page and request page to something more modern in terms of the layout/form design and with more content, but needs to be consistent with the rest of our site. I need two pages designed. 1) A general pricing page w/ CTAs for quotes, and 2) The request quote page with form. Ideally there would be (3) parts for our different packages (Express, Professional, Enterprise) on the pricing page, with CTAs on each section. I like the hero image approach used here https://plovane.com/pricing and here http://www.gridmarrow.com/wp-content/uploads/2016/08/corvalink-pricing-page-design.png In terms of the form page, mainly just looking for an improvement over this https://www.lumadrift.com/price-quote-request

I also included a sample mockup to provide a BIT of guidance, but looking for something a little different and modern.

Industry/Entity Type

Pricing

Number of Pages Required

2 page

Font styles to use
Sans Serif

Requirements
Must have
• Hero background image on main pricing page. Needs to follow the look and feel of lumadrift.com

```html
<!DOCTYPE html>
<html lang="en">
<head>
<meta charset="utf-8">
<title>Request Quote</title>
<link href="https://fonts.googleapis.com/css2?family=Hind:wght@300;400;500;600;700&display=swap" rel="stylesheet">
<style>
  :root {
    --ink: #ffffff;
    --muted: #c9c9c9;
    --accent: #8cc43f;
    --accent-dark: #6f9a33;
    --panel: #000000;
    --field: #e6e6e6;
    --header: rgba(0, 0, 0, 0.62);
    --footer-text: #a8a8a8;
  }
  * { box-sizing: border-box; margin: 0; padding: 0; }
  html, body { width: 1200px; height: 742px; overflow: hidden; }
  body {
    position: relative;
    font-family: "Hind", Arial, sans-serif;
    color: var(--ink);
    background: #1e1a15;
  }
  .hero-photo {
    position: absolute; inset: 0;
    background:
      radial-gradient(ellipse at 45% 45%, #4a3b2b 0%, #2f261d 45%, #1a1612 100%);
  }
  .hero-shade { position: absolute; inset: 0; background: rgba(0,0,0,0.35); }

  .site-header {
    position: absolute; left: 0; top: 0; width: 1200px; height: 98px;
    background: var(--header);
  }
  .brand {
    position: absolute; left: 60px; top: 30px; height: 38px;
    display: flex; align-items: center; gap: 10px;
    font-size: 18px; font-weight: 500; letter-spacing: 1px; color: var(--ink);
  }
  .brand-square { width: 14px; height: 14px; background: var(--ink); }

  .main-nav { position: absolute; top: 38px; left: 0; width: 1200px; height: 22px; }
  .main-nav a {
    position: absolute; transform: translateX(-50%);
    font-size: 14px; color: var(--muted); text-decoration: none; line-height: 22px;
  }
  .main-nav a.active { color: var(--ink); }
  .main-nav a.active::after {
    content: ""; position: absolute; left: -7px; right: -7px; top: 29px;
    height: 4px; background: var(--accent);
  }
  .demo-button {
    position: absolute; left: 950px; top: 30px; width: 190px; height: 36px;
    background: var(--accent); color: var(--ink);
    font-size: 14px; font-weight: 600; letter-spacing: 0.3px;
    display: flex; align-items: center; justify-content: center;
  }

  .intro { position: absolute; left: 60px; top: 228px; width: 560px; }
  .intro h1 { font-size: 40px; font-weight: 700; line-height: 1; }
  .intro .lead { margin-top: 26px; font-size: 16px; line-height: 25px; }
  .intro h2 { margin-top: 14px; font-size: 15.5px; font-weight: 600; color: var(--accent); }
  .factors { list-style: none; margin-top: 9px; font-size: 13px; }
  .factors li { height: 31.3px; line-height: 20px; }
  .factors li::before { content: "• "; }

  .quote-panel {
    position: absolute; left: 762px; top: 197px; width: 363px; height: 424px;
    background: var(--panel);
  }
  .quote-panel h2 {
    position: absolute; left: 39px; top: 30px;
    font-size: 31px; font-weight: 300; letter-spacing: 0.3px; line-height: 1;
  }
  .quote-panel input {
    position: absolute; left: 41px; width: 285px; height: 35px;
    border: 0; background: var(--field);
  }
  .submit-button {
    position: absolute; left: 41px; top: 357px; width: 285px; height: 46px;
    border: 0; background: var(--accent-dark); color: #000;
    font-family: "Hind", Arial, sans-serif; font-size: 19px; font-weight: 500; letter-spacing: 0.8px;
    padding-top: 3px;
  }

  .copyright {
    position: absolute; left: 0; width: 1200px; top: 704px; text-align: center;
    font-family: Arial, Helvetica, sans-serif; font-size: 13px; color: var(--footer-text);
  }
</style>
</head>
<body>
  <div class="hero-photo" role="img" aria-label="Overhead photo of a team working around a wooden table with laptops, keyboards, papers and coffee cups"></div>
  <div class="hero-shade"></div>

  <header class="site-header">
    <div class="brand"><span class="brand-square"></span>YOUR BUSINESS</div>
    <nav class="main-nav">
      <a class="active" style="left:429px">HOME</a>
      <a style="left:512px">ABOUT</a>
      <a style="left:612px">SERVICES</a>
      <a style="left:714px">WORK</a>
      <a style="left:805px">CONTACT</a>
      <a style="left:893px">BLOG</a>
    </nav>
    <div class="demo-button">REQUEST DEMO</div>
  </header>

  <section class="intro">
    <h1>Request Quote</h1>
    <p class="lead">Our pricing structures are unique to each business.Depending on your requirements, we will build out a model which works for you.</p>
    <h2>Pricing is typically based on these factors:</h2>
    <ul class="factors">
      <li>Number of instances needed (websites)</li>
      <li>Amount of courses to be created</li>
      <li>Number of users accessing those courses</li>
      <li>Seat/active user model, whichever works best</li>
    </ul>
  </section>

  <form class="quote-panel">
    <h2>Quote Details</h2>
    <input type="text" aria-label="Name" style="top:81px">
    <input type="text" aria-label="Company" style="top:126px">
    <input type="email" aria-label="Email" style="top:169px">
    <input type="tel" aria-label="Phone" style="top:214px">
    <input type="text" aria-label="Number of users" style="top:258px">
    <input type="text" aria-label="Message" style="top:303px">
    <button class="submit-button" type="button">SUBMIT</button>
  </form>

  <footer class="copyright">Copyright © 2016 Your Business. All Right Reserved.</footer>
</body>
</html>
```